School teacher strategies for teachers to improve their lessons.

This is for displays for teachers in their office about how to best teach students. This should be styled in a professional way that aligns with the colour themes of the school.

For reference, here is the school's website:
https://tallowmeresc.qz.edu.au/

I have attached a previous document "Steady Habits" - please use similar theme.

Target Market(s)

teachers at this school

Colors

Requirements
Must have
• School logo. And aligned to previous designs

```html
<!DOCTYPE html>
<html lang="en">
<head>
<meta charset="utf-8">
<title>Tallowmere Instructional Model — Learning Goal &amp; Success Criteria</title>
<link href="https://fonts.googleapis.com/css2?family=Poppins:wght@400;500;600;700;800&display=swap" rel="stylesheet">
<style>
:root{
  --navy:#0f3f86;
  --navy-deep:#0c3675;
  --yellow:#f6dd6a;
  --yellow-line:#f3d94d;
  --paper:#f3f3f3;
  --white:#ffffff;
  --ink:#1b1b1b;
  --muted:#bfbfc7;
  --rule:#d8d8d8;
}
*{box-sizing:border-box;margin:0;padding:0}
html,body{width:995px;height:1200px;overflow:hidden}
body{font-family:"Poppins",sans-serif;color:var(--ink);background:var(--white)}
.poster{width:995px;height:1200px;display:flex;flex-direction:column}

/* header */
.masthead{height:384px;display:flex}
.brand-panel{width:288px;background:var(--paper);padding:42px 28px 0 60px;display:flex;flex-direction:column;align-items:center}
.school-name{margin-top:62px;display:flex;align-items:center;gap:10px;font-weight:700;font-size:22px;color:var(--navy)}
.school-name .dot{width:18px;height:18px;border-radius:50%;background:var(--yellow-line)}
.formula{margin-top:78px;width:200px;border-radius:10px;overflow:hidden;background:var(--navy)}
.formula-label{background:var(--muted);color:var(--navy);font-weight:700;font-size:10.5px;padding:6px 16px}
.formula-body{color:var(--white);font-size:11.5px;line-height:1.45;padding:12px 16px 14px;text-transform:uppercase}
.formula-body strong{display:block;margin-top:8px;font-weight:700;font-size:12px}
.title-panel{flex:1;background:var(--navy);padding:40px 58px 0 30px;color:var(--white)}
.title-panel h1{font-weight:800;font-size:30.5px;line-height:1.17;letter-spacing:-.2px}
.purpose{margin-top:10px;font-size:11.5px;line-height:1.6}
.example{margin-top:22px;display:flex;border:1.5px solid var(--yellow-line);border-radius:8px;overflow:hidden;height:52px}
.example + .example{margin-top:22px}
.example-tag{width:62px;background:var(--yellow);color:var(--ink);text-align:center;font-weight:600;font-size:10px;padding-top:5px;line-height:1.1}
.example-tag b{display:block;font-size:24px;font-weight:700}
.example p{flex:1;padding:6px 10px;font-size:11.5px;line-height:1.55}

/* checklist */
.essentials{height:215px;display:flex;background:var(--white)}
.checklist{flex:1;padding:16px 0 0 60px}
h2{color:var(--navy);font-weight:700;font-size:12.5px;text-transform:uppercase}
.checklist ul{list-style:none;margin-top:8px}
.checklist li{display:flex;align-items:center;gap:9px;font-size:10.2px;height:22px}
.checklist svg{flex:none}
.photo{width:388px;background:linear-gradient(120deg,#7e6b55 0%,#c9c2b4 35%,#f2efe8 55%,#8d6e52 100%)}

/* success criteria */
.criteria{height:393px;background:var(--paper);padding:16px 60px 0}
.criteria h2{font-size:15px}
.criteria .lead{margin-top:10px;font-size:11.2px;line-height:1.65;max-width:770px}
.cards{margin-top:20px;display:flex;gap:32px}
.card{flex:1;background:var(--white);border-radius:10px;height:200px;overflow:hidden;box-shadow:0 1px 4px rgba(0,0,0,.08)}
.card h3{background:var(--yellow);font-weight:700;font-size:11.5px;padding:11px 14px;text-transform:uppercase}
.card ul{list-style:none;padding:6px 14px 0}
.card li{position:relative;padding:7px 0 7px 14px;font-size:10.2px;line-height:1.6;border-bottom:1px solid var(--rule)}
.card li:last-child{border-bottom:none}
.card li::before{content:"";position:absolute;left:0;top:13px;width:5px;height:5px;border-radius:50%;background:var(--navy)}
.card li b{color:var(--navy);font-weight:700}
.criteria .note{margin-top:18px;font-size:11.2px;line-height:1.65;max-width:760px}

/* embed */
.embed{height:115px;background:var(--yellow);padding:20px 60px 0}
.embed h2{color:var(--ink);font-size:13.5px}
.embed p{font-size:13.5px;color:var(--navy);margin-top:6px}
.embed p + p{margin-top:5px}

/* footer */
.contact{height:93px;background:var(--navy);border-top:3px solid var(--white);display:flex;align-items:center;padding:0 46px 0 60px;color:var(--white)}
.contact-item{display:flex;align-items:center;gap:12px}
.address{font-size:12.5px;line-height:1.45;width:242px}
.phone{font-size:21px;width:228px}
.email{font-size:13.5px}
</style>
</head>
<body>
<main class="poster">
  <header class="masthead">
    <section class="brand-panel">
      <div class="school-name"><span class="dot"></span>Tallowmere</div>
      <div class="formula">
        <div class="formula-label">USE THIS ONE LINE FORMULA</div>
        <div class="formula-body">By the end of the lesson, students will
          <strong>[verb] [skill/concept]* [conditions/context].</strong>
        </div>
      </div>
    </section>
    <section class="title-panel">
      <h1>TALLOWMERE INSTRUCTIONAL MODEL — WRITE A POWERFUL LEARNING GOAL &amp; SUCCESS CRITERIA</h1>
      <p class="purpose">Purpose: This poster guides staff to craft clear Learning Goals and Success Criteria aligned to How Tallowmere Students Learn.</p>
      <div class="example">
        <div class="example-tag">EXAMPLE<b>01</b></div>
        <p>By the end of the lesson, students will apply Pythagoras’ theorem to find the hypotenuse of a right triangle with integer side lengths.</p>
      </div>
      <div class="example">
        <div class="example-tag">EXAMPLE<b>02</b></div>
        <p>By the end of the lesson, students will describe two factors that influence liveability in their local area using evidence from a map.</p>
      </div>
    </section>
  </header>

  <section class="essentials">
    <div class="checklist">
      <h2>Essentials Checklist</h2>
      <ul>
        <li><svg width="12" height="12" viewBox="0 0 12 12"><rect x="1" y="2" width="9" height="9" fill="none" stroke="#0f3f86" stroke-width="1.4"/><path d="M3 6l2.5 2.5L11 1.5" fill="none" stroke="#0f3f86" stroke-width="1.6"/></svg>About learning, not tasks: focus on knowledge/skill students will learn today.</li>
        <li><svg width="12" height="12" viewBox="0 0 12 12"><rect x="1" y="2" width="9" height="9" fill="none" stroke="#0f3f86" stroke-width="1.4"/><path d="M3 6l2.5 2.5L11 1.5" fill="none" stroke="#0f3f86" stroke-width="1.6"/></svg>Right verb, right level: choose a precise Bloom’s/cognitive verb.</li>
        <li><svg width="12" height="12" viewBox="0 0 12 12"><rect x="1" y="2" width="9" height="9" fill="none" stroke="#0f3f86" stroke-width="1.4"/><path d="M3 6l2.5 2.5L11 1.5" fill="none" stroke="#0f3f86" stroke-width="1.6"/></svg>One idea only: keep scope tight to manage cognitive load.</li>
        <li><svg width="12" height="12" viewBox="0 0 12 12"><rect x="1" y="2" width="9" height="9" fill="none" stroke="#0f3f86" stroke-width="1.4"/><path d="M3 6l2.5 2.5L11 1.5" fill="none" stroke="#0f3f86" stroke-width="1.6"/></svg>Student friendly: plain language students can restate; accessible to all students.</li>
        <li><svg width="12" height="12" viewBox="0 0 12 12"><rect x="1" y="2" width="9" height="9" fill="none" stroke="#0f3f86" stroke-width="1.4"/><path d="M3 6l2.5 2.5L11 1.5" fill="none" stroke="#0f3f86" stroke-width="1.6"/></svg>Visible &amp; revisited: display it; say it at transitions and again during the review at lesson end.</li>
        <li><svg width="12" height="12" viewBox="0 0 12 12"><rect x="1" y="2" width="9" height="9" fill="none" stroke="#0f3f86" stroke-width="1.4"/><path d="M3 6l2.5 2.5L11 1.5" fill="none" stroke="#0f3f86" stroke-width="1.6"/></svg>Assessable: design quick checks and an exit slip that align to the Success Criteria.</li>
        <li><svg width="12" height="12" viewBox="0 0 12 12"><rect x="1" y="2" width="9" height="9" fill="none" stroke="#0f3f86" stroke-width="1.4"/><path d="M3 6l2.5 2.5L11 1.5" fill="none" stroke="#0f3f86" stroke-width="1.6"/></svg>Same Learning Goal for all; differentiate supports (scaffolds/groups), not the intention.</li>
      </ul>
    </div>
    <div class="photo" role="img" aria-label="Photo of two uniformed students reading books in the school library"></div>
  </section>

  <section class="criteria">
    <h2>Success Criteria: Curriculum &amp; Behaviour (What / How / Why)</h2>
    <p class="lead">Write two short sets of success criteria so students are clear on what they’re learning and how they’ll behave to achieve it — and why each matters (aligned with Classroom Profiling).</p>
    <div class="cards">
      <article class="card">
        <h3>Curriculum (Learning)</h3>
        <ul>
          <li><b>What:</b> the specific knowledge/skill linked to today’s learning goal.</li>
          <li><b>How:</b> the routine/strategy students will use to demonstrate it (e.g., worked example steps, analysis routine, calculation method).</li>
          <li><b>Why:</b> the purpose or connection (e.g., links to the next lesson/ assessment; helps solve real problems).</li>
        </ul>
      </article>
      <article class="card">
        <h3>Behaviour (Learning Behaviours)</h3>
        <ul>
          <li><b>What:</b> the explicit behaviour expectation (e.g., track the speaker; voice level; hands/signals).</li>
          <li><b>How:</b> the routine to meet it (e.g., attention signal → pause → response; partner roles; “Ask 3 before me).</li>
          <li><b>Why:</b> maximises learning time, safety, and fairness for everyone.</li>
        </ul>
      </article>
    </div>
    <p class="note">Keep each bullet student friendly and observable ("I can" statements). Plan a quick check for each “How” and revisit both sets in the review.</p>
  </section>

  <section class="embed">
    <h2>Embed the Goal in the Tallowmere Instructional Model</h2>
    <p>Warm up (activate) → I Do → We Do → You Do It Together → You Do → Review goal &amp; success criteria</p>
    <p>• Use evidence from checks to loop back or release (don’t push on if the evidence says pause).</p>
  </section>

  <footer class="contact">
    <div class="contact-item address">
      <svg width="28" height="36" viewBox="0 0 28 36"><path d="M14 0C6.3 0 0 6 0 13.5 0 23 14 36 14 36s14-13 14-22.5C28 6 21.7 0 14 0z" fill="#fff"/><circle cx="14" cy="13" r="5.5" fill="#0f3f86"/></svg>
      <span>48-60 Harrow Lane<br>Kellbrook QLD 4390, Australia</span>
    </div>
    <div class="contact-item phone">
      <svg width="30" height="30" viewBox="0 0 24 24"><path d="M6.6 10.8a15.1 15.1 0 0 0 6.6 6.6l2.2-2.2c.3-.3.7-.4 1-.2 1.1.4 2.3.6 3.6.6.6 0 1 .4 1 1V20c0 .6-.4 1-1 1A17 17 0 0 1 3 4c0-.6.4-1 1-1h3.5c.6 0 1 .4 1 1 0 1.3.2 2.5.6 3.6.1.3 0 .7-.2 1z" fill="#fff"/><path d="M14 2.5a8 8 0 0 1 7.5 7.5M14 6a4.5 4.5 0 0 1 4 4" fill="none" stroke="#fff" stroke-width="1.5"/></svg>
      <span>(07) 3555 0142</span>
    </div>
    <div class="contact-item email">
      <svg width="24" height="18" viewBox="0 0 24 18"><rect x="1" y="1" width="22" height="16" fill="none" stroke="#fff" stroke-width="1.8"/><path d="M1 1l11 9 11-9M1 17l8-7M23 17l-8-7" fill="none" stroke="#fff" stroke-width="1.6"/></svg>
      <span>principal@tallowmeresc.qz.edu.au</span>
    </div>
  </footer>
</main>
</body>
</html>
```